Aggressive Appliance retailer requires a Large Billboard design.

We require a large Tall billboard design it stands 4500mm high x 2400mm across. We have our own range of imported appliances called Velomardi and we provide a 5 year warranty, key pionts low price + long solid warranty. Provided are 3 products 1 x clothes washer 8 kg $699 1 x dishwasher $499 1 x side by side fridge freezer $1299 all with 5 year warranty. Company colors very bright green. Provided warranty logo / images / and an add that has the font we have preference too. I am not rigid to the above requirements and open to designers own ideas :-) I have supplied a few dishwasher images if you want one with closed door i may need to sort one out

```html
<!DOCTYPE html>
<html lang="en">
<head>
<meta charset="utf-8">
<title>Velomardi Spring/Summer Blowout Billboard</title>
<link href="https://fonts.googleapis.com/css2?family=Bangers&family=Roboto:ital,wght@0,700;0,900;1,700&display=swap" rel="stylesheet">
<style>
  :root{
    --page:#e4e5e7;
    --sky-top:#f2ea1e;
    --sky-bottom:#8cc63f;
    --green:#2fb34b;
    --dark-green:#0d4d1e;
    --red:#c6374e;
    --ink:#111;
    --white:#fff;
    --yellow:#ffe600;
    --price-red:#e0262a;
    --steel:#b9bcc0;
  }
  html,body{margin:0;width:1200px;height:1000px;overflow:hidden;background:var(--page);}
  .billboard{position:absolute;left:340px;top:38px;width:490px;height:918px;background:var(--white);overflow:hidden;font-family:"Bangers",cursive;}
  .billboard-field{position:absolute;left:0;top:0;width:490px;height:814px;background:linear-gradient(180deg,var(--sky-top) 0%,#d6e130 45%,var(--sky-bottom) 100%);}
  .abs{position:absolute;}
  .outlined{paint-order:stroke fill;-webkit-text-stroke:5px var(--ink);}
  .flower-row{left:14px;top:2px;width:462px;height:62px;border-radius:20px;background:linear-gradient(90deg,#7b3fa8,#e8308f,#d93a4a,#f05a28,#27a8e0,#7b3fa8,#f05a28);opacity:.85;}
  .headline{left:0;width:490px;text-align:center;margin:0;line-height:1;white-space:nowrap;}
  .headline-season{top:62px;font-size:60px;letter-spacing:5px;color:var(--green);-webkit-text-stroke:7px var(--ink);paint-order:stroke fill;transform:rotate(-2deg);}
  .headline-blowout{top:112px;font-size:104px;letter-spacing:10px;color:var(--red);-webkit-text-stroke:8px var(--ink);paint-order:stroke fill;}
  .headline-sub{top:204px;font-size:36px;letter-spacing:3px;color:var(--white);}
  .product-title{margin:0;font-size:27px;line-height:25px;letter-spacing:2.5px;color:var(--green);white-space:nowrap;}
  .product-title small{font-size:15px;}
  .spec{margin:0;font-family:"Roboto",sans-serif;font-style:italic;font-weight:700;font-size:12px;line-height:16px;color:var(--white);-webkit-text-stroke:2px var(--ink);paint-order:stroke fill;white-space:nowrap;}
  .photo{border-radius:4px;}
  .photo-washer{left:18px;top:345px;width:112px;height:142px;background:linear-gradient(160deg,#eef0f2,#9ea3a8);}
  .photo-dishwasher{left:355px;top:347px;width:117px;height:145px;background:linear-gradient(160deg,#f4f6f8,#aeb3b8);}
  .photo-fridge{left:18px;top:617px;width:92px;height:160px;background:linear-gradient(90deg,#d7dadd,#9aa0a5,#d7dadd);}
  .price-burst{width:92px;height:92px;border-radius:50%;background:var(--white);box-shadow:4px 4px 0 var(--price-red),5px 5px 0 var(--ink);display:flex;flex-direction:column;align-items:center;justify-content:center;transform:rotate(-10deg);}
  .price-label{font-size:24px;line-height:22px;color:var(--yellow);-webkit-text-stroke:4px var(--ink);paint-order:stroke fill;}
  .price-value{font-size:34px;line-height:32px;color:var(--price-red);-webkit-text-stroke:4px var(--yellow);paint-order:stroke fill;}
  .warranty-head{left:270px;top:546px;width:200px;text-align:center;margin:0;font-size:36px;line-height:36px;letter-spacing:3px;color:var(--white);}
  .warranty-badge{left:300px;top:622px;width:138px;height:143px;border-radius:14px;background:linear-gradient(160deg,#e3e5e8,var(--steel) 60%,#8d9196);box-shadow:2px 3px 4px rgba(0,0,0,.35);}
  .footer{left:0;top:814px;width:490px;height:104px;background:var(--white);}
  .brand{left:20px;top:26px;display:flex;align-items:center;gap:8px;}
  .brand-mark{width:14px;height:14px;background:var(--green);}
  .brand-name{font-family:"Bangers",cursive;font-size:46px;line-height:50px;color:var(--ink);letter-spacing:1px;}
  .contact{left:190px;top:8px;width:280px;text-align:center;color:var(--green);-webkit-text-stroke:3px var(--dark-green);paint-order:stroke fill;white-space:nowrap;}
  .contact p{margin:0;line-height:1;}
  .contact .address{font-size:18px;letter-spacing:2px;}
  .contact .phone{font-size:27px;letter-spacing:2px;}
  .contact .cards{font-size:11px;letter-spacing:1px;-webkit-text-stroke:2px var(--dark-green);}
  .contact .hours{font-size:25px;letter-spacing:3px;margin-top:3px;}
</style>
</head>
<body>
<main class="billboard">
  <div class="billboard-field"></div>
  <div class="abs flower-row" role="img" aria-label="Row of colourful cartoon spring flowers and tulips"></div>

  <h1 class="abs headline headline-season">Spring/Summer</h1>
  <h1 class="abs headline headline-blowout">Blowout</h1>
  <h2 class="abs headline headline-sub outlined">On all major appliances</h2>

  <section class="product product-washer">
    <h3 class="abs product-title outlined" style="left:15px;top:287px;">Velomardi<br>Clothes Washer</h3>
    <p class="abs spec" style="left:130px;top:344px;">Weighs 8 Kg</p>
    <div class="abs photo photo-washer" role="img" aria-label="Top-loading clothes washer"></div>
    <div class="abs price-burst" style="left:118px;top:392px;"><span class="price-label">Only</span><span class="price-value">$699</span></div>
  </section>

  <section class="product product-dishwasher">
    <h3 class="abs product-title outlined" style="left:262px;top:287px;">Velomardi<br>Dishwasher</h3>
    <p class="abs spec" style="left:265px;top:344px;">Large<br>Capacity</p>
    <div class="abs photo photo-dishwasher" role="img" aria-label="White freestanding dishwasher"></div>
    <div class="abs price-burst" style="left:276px;top:398px;"><span class="price-label">Compare</span><span class="price-value">$499</span></div>
  </section>

  <section class="product product-fridge">
    <h3 class="abs product-title outlined" style="left:15px;top:534px;">Velomardi<br>Side <small>by</small> Side<br>Fridge/Freezer</h3>
    <p class="abs spec" style="left:126px;top:618px;">570 Litre<br>Frost-Free<br>Stainless-Steel Exterior</p>
    <div class="abs photo photo-fridge" role="img" aria-label="Stainless-steel side by side fridge freezer"></div>
    <div class="abs price-burst" style="left:114px;top:668px;"><span class="price-label">Low</span><span class="price-value">$1299</span></div>
  </section>

  <h2 class="abs warranty-head outlined">All<br>Come with</h2>
  <div class="abs warranty-badge" role="img" aria-label="Five year comprehensive warranty badge"></div>

  <footer class="abs footer">
    <div class="abs brand"><span class="brand-mark"></span><span class="brand-name">Velomardi</span></div>
    <div class="abs contact">
      <p class="address">4821 Meadowbank Road</p>
      <p class="phone">Phone: 555-0142</p>
      <p class="cards">All major credit cards accepted</p>
      <p class="hours">Open 9-9 Mon - Fri</p>
    </div>
  </footer>
</main>
</body>
</html>
```